folding sales brochure

We need a brochure in the colors of orange, black and charcoal gray - our logo colors.
www.venbrooklinguaservices

Strong, clean - and something eye catching.

We are looking for graphic images and photos that depict international business, written translation, live simultaneous interpretation for conferences & events with people communicating. We have some photos, but are open to others.

This brochure will generalize our companies services.
This brochure will be used for B2B as well as Trade Show booths.

Reason: Project has been extended to allow time for feedback and completion. Thank you all... some wonderful designs.

Thank you all for your designs - they were all creative in so many different ways, making the choice of just one very difficult.

regards,
Dorela

Target Market(s)

Our target is large global corporate companies.

Industry/Entity Type

Events

Requirements
Must have
• company logo (will supply)
company website and address etc.

Our Type Font is: Helvetica Neue LT Std

All info needed can be found here: www.venbrooklinguaservices
Should not have
• we feel globes and flags are overdone in the International marketplace - hopefully you can find something else to speak Global.

```html
<!DOCTYPE html>
<html lang="en">
<head>
<meta charset="utf-8">
<title>Venbrook Lingua Services – Tri-fold Brochure</title>
<link href="https://fonts.googleapis.com/css2?family=Roboto:wght@300;400&family=Josefin+Sans:wght@300&display=swap" rel="stylesheet">
<style>
:root{
  --stage:#2e2e2e;
  --orange:#e8892a;
  --charcoal:#2a2a2a;
  --black:#111;
  --paper:#ffffff;
  --panel-grey:#ececec;
  --ink:#3a3a3a;
  --white:#fff;
}
*{margin:0;padding:0;box-sizing:border-box}
html,body{width:1200px;height:1000px;overflow:hidden;background:var(--stage)}
.canvas{position:relative;width:1200px;height:1000px;font-family:"Roboto",Arial,sans-serif;font-weight:300}
.spread{position:absolute;background:var(--paper)}
.spread--front{left:315px;top:32px;width:570px;height:440px}
.spread--inside{left:315px;top:518px;width:571px;height:440px}
.panel{position:absolute;overflow:hidden}
.panel--orange{background:var(--orange);color:var(--white)}
.panel--white{background:var(--paper);color:var(--ink)}
.panel--grey{background:var(--panel-grey);color:var(--ink)}
.panel--dark{background:linear-gradient(180deg,#1a1a1a 0%,#2b2b2b 35%,#6a6a6a 62%,#2a2a2a 85%,#151515 100%);color:var(--white)}
.heading{position:absolute;font-weight:300;font-size:12px;line-height:16px;white-space:nowrap}
.heading--tab::before{content:"";position:absolute;left:-14px;top:-2px;width:6px;height:20px;background:var(--white)}
.heading--orange{color:var(--orange)}
.heading--dark{color:var(--charcoal)}
.copy{position:absolute;font-size:6.7px;line-height:9.4px;font-weight:300}
.copy p+p{margin-top:9.4px}
.copy--inside{line-height:12.9px}
.copy--inside p+p{margin-top:12.9px}
.photo{position:absolute}
.brand{position:absolute;display:flex;align-items:center;justify-content:center;gap:7px;font-weight:300;font-size:19px;letter-spacing:.5px}
.brand__dot{width:16px;height:16px;border-radius:50%;background:var(--orange)}
.brand--on-black{background:var(--black);color:var(--white)}
.brand--on-white{background:var(--white);color:var(--charcoal)}
.contact{position:absolute;font-size:6.6px;line-height:10.2px;font-weight:300;color:var(--ink);font-style:normal}
.contact .accent{color:var(--orange)}
.tagline{position:absolute;width:100%;text-align:center;font-weight:300}
.label{position:absolute;font-family:"Josefin Sans",Arial,sans-serif;font-weight:300;color:var(--white);font-size:34px;letter-spacing:1px}
</style>
</head>
<body>
<main class="canvas">

  <section class="spread spread--front">
    <article class="panel panel--orange" style="left:5px;top:5px;width:178px;height:430px">
      <h2 class="heading heading--tab" style="left:14px;top:20px">What We Do</h2>
      <div class="copy" style="left:14px;top:43px;width:160px">
        <p>Language solutions for today</p>
        <p>"Language Solutions" are the services that allow communication to transcend language barriers. We begin with translators and interpreters and finish with the technology to bring it all together.</p>
        <p>Our solutions are just that: answers to problems. We meet your needs so you don't have to worry. Through Venbrook, you communicate with your global audience with equal respect.</p>
        <p>We are a nationwide leader in live event language services, which includes simultaneous interpreters, interpreting equipment, and push-to-talk discussion systems. Our translation division has decades of experience and millions of words under its belt. Today, these services include a full range of studio services like voiceover and subtitles.</p>
      </div>
      <div class="photo" role="img" aria-label="Close-up photo of a keyboard with language-name keys and a blue Translate key" style="left:0;top:226px;width:178px;height:97px;background:linear-gradient(160deg,#4a4a4a,#1c1c1c 55%,#2c3e66 80%,#1a1a1a)"></div>
      <h2 class="heading heading--tab" style="left:14px;top:332px">Why Choose Us</h2>
      <div class="copy" style="left:14px;top:356px;width:160px">
        <p>More than capable, we make it easy.</p>
        <p>Our approach is based on core principles of dedication, innovation and being prepared. Our clients' satisfaction matters the most, and we know that can only be guaranteed if we are prepared for any situation.</p>
      </div>
    </article>

    <article class="panel panel--white" style="left:192px;top:0;width:186px;height:440px">
      <h2 class="heading heading--orange" style="left:9px;top:25px">Our History</h2>
      <div class="copy" style="left:9px;top:50px;width:172px">
        <p>Venbrook Lingua Services, formerly Meridian Conference Services, began in 1997 as the conference interpreting division of Meridian Translating Services. Today, it also includes the written translation division of Meridian Translating Services, following in a tradition going back to 1984.</p>
        <p>In 2005, we became the first company in North America to acquire the 32-language Halvern Orion Series interpreting system. Now as the largest dedicated interpretation and discussion rental provider in the US, we continue to pioneer new approaches, embrace new technologies, and set new standards in customer service.</p>
      </div>
      <div class="brand brand--on-black" style="left:63px;top:202px;width:123px;height:56px"><span class="brand__dot"></span>venbrook</div>
      <address class="contact" style="left:63px;top:276px">
        Venbrook Lingua <span class="accent">Services</span><br>
        4120 Harbor Ridge Road, Unit 210<br>
        Larkfield, CA 91402<br><br>
        Mailing address:<br>
        P.O. Box 552817<br>
        Larkfield, CA 91409<br><br>
        Phone:+1 555 210 4471<br><br>
        Toll free:+1 888 555 0142<br>
        Fax:+1 866 555 0187<br>
        Email:click to reveal@venbrook.us
      </address>
    </article>

    <article class="panel panel--dark" style="left:385px;top:5px;width:180px;height:430px">
      <div class="photo" role="img" aria-label="Photo of an antique world globe lit warmly against a dark background" style="left:0;top:113px;width:180px;height:155px;background:radial-gradient(circle at 50% 60%,#c9893a 0%,#7a4a1c 38%,#2a1a0e 70%,#111 100%)"></div>
      <div class="brand brand--on-white" style="left:63px;top:197px;width:117px;height:56px"><span class="brand__dot"></span>venbrook</div>
      <p class="tagline" style="top:395px;font-size:9.5px">Helping you speak to the world</p>
      <p class="tagline" style="top:411px;font-size:8.5px;color:var(--orange)">www.venbrooklinguaservices.com</p>
    </article>
  </section>

  <section class="spread spread--inside">
    <article class="panel panel--orange" style="left:5px;top:5px;width:178px;height:430px">
      <h2 class="heading heading--tab" style="left:9px;top:20px">Event Services</h2>
      <div class="copy copy--inside" style="left:9px;top:49px;width:162px">
        <p>We specialize in live events featuring simultaneous conference interpreting, translation equipment rental and/or push to talk discussion and voting systems.</p>
        <p>As opposed to translation, which is the term applied to the written form of translation between languages, simultaneous interpretation is the term used for the specific skill of verbally translating from one language to another in real time. This is achieved by pairing highly skilled conference interpreters with the specialized equipment necessary for them to able to perform accurately and to their best abilities.</p>
      </div>
      <div class="photo" role="img" aria-label="Photo of a conference panel seated at a long table before a blue projection screen" style="left:0;top:204px;width:178px;height:105px;background:linear-gradient(180deg,#2d6fa8 0%,#1d4f80 45%,#222 70%,#0d0d0d 100%)"></div>
      <div class="copy copy--inside" style="left:9px;top:311px;width:164px">
        <p>Limiting purely to events over 2000 attendees and in the past 3 years alone, Venbrook has globally provided rental of simultaneous interpretation equipment, personnel and services at over 60 events, averaging 14.5k attendees each for a total of over 600,000 people in up to 27 languages at a time. Aside from shipping equipment around the world every week, we maintain a rental stock in the UK, allowing us to provide direct local service and support to our clients in Europe.</p>
      </div>
    </article>

    <article class="panel panel--grey" style="left:195px;top:5px;width:178px;height:430px">
      <h2 class="heading heading--tab heading--dark" style="left:10px;top:20px">Interpreting Services</h2>
      <div class="copy" style="left:10px;top:50px;font-size:6.8px">Only the best interpreters…</div>
      <div class="photo" role="img" aria-label="Photo of business people in suits talking together in a bright office" style="left:0;top:61px;width:178px;height:91px;background:linear-gradient(135deg,#dfe6ec 0%,#9aa8b4 40%,#3c4650 70%,#c9d2da 100%)"></div>
      <div class="copy copy--inside" style="left:10px;top:153px;width:162px">
        <p>We take special care to find the very best interpreters working today. We always use interpreters who are members of the Global Guild of Conference Interpreters (GGCI) or of an equally accredited organization. Our conference interpreters have extensive training in the very specialized skill of simultaneous interpretation. We also specialize in consecutive, over-the-phone and tour guide interpreters. We appreciate that the quality of interpretation is the keystone of a multilingual event, and we don't leave it to chance.</p>
      </div>
      <h2 class="heading heading--dark" style="left:10px;top:306px">Remote interpreting</h2>
      <div class="photo" role="img" aria-label="Small photo of business people in conversation" style="left:151px;top:300px;width:27px;height:24px;background:linear-gradient(135deg,#e6e9ec,#4b5560)"></div>
      <div class="copy copy--inside" style="left:10px;top:335px;width:162px">
        <p>Synergy in action: pulling from our experience with live events, interpreting, and audio technology, we offer a new kind of service. We can provide you with a live, simultaneous interpretation of your event or teleconference remotely from our facilities. This is especially useful for international conference calls, small events or those held on short notice.</p>
      </div>
    </article>

    <article class="panel panel--orange" style="left:385px;top:5px;width:181px;height:430px">
      <h2 class="heading heading--tab" style="left:10px;top:20px">Translation Services</h2>
      <div class="photo" role="img" aria-label="Small photo of a lit world globe" style="left:130px;top:16px;width:51px;height:24px;background:radial-gradient(circle at 50% 60%,#c98a3c,#3a2412 70%)"></div>
      <div class="copy copy--inside" style="left:10px;top:50px;width:166px">
        <p>Your written translations deserve the same care, study and professionalism as the original text. We have over a decade of providing written translations to some of the largest companies and organizations in the world, in nearly every language. Our translators are certified in their field and are specialized in their subject matter. Our additional services include multilingual design and layout, website translation and software localization.</p>
      </div>
      <h2 class="heading heading--tab" style="left:10px;top:161px">Audio visual tour apps</h2>
      <div class="photo" role="img" aria-label="Small photo of a smartphone" style="left:129px;top:157px;width:52px;height:26px;background:linear-gradient(135deg,#f0f0f0,#2a2a2a 55%,#555)"></div>
      <div class="copy copy--inside" style="left:10px;top:191px;width:164px">
        <p>Leveraging our in house multilingual studio services and in house app development expertise, we can supply you a customized, branded application to be delivered on the platform of your choice.</p>
      </div>
      <h2 class="heading heading--tab" style="left:10px;top:256px">Studio Services</h2>
      <div class="photo" role="img" aria-label="Small photo of a studio microphone" style="left:100px;top:250px;width:81px;height:47px;background:radial-gradient(circle at 40% 45%,#8a8a8a,#2a2a2a 60%,#111)"></div>
      <div class="copy copy--inside" style="left:10px;top:285px;width:166px">
        <p>Multilingual studio services<br>Access to a modern, professional studio is a necessity in order for clients to communicate with a global audience via traditional media or the internet. Whether you need to dub a recording, produce an original spot, or subtitle a video, we are ready with a solution. Using some of Hollywood's best voice talent, we produce professional voiceovers in any language. We also specialize in providing translations for film and TV productions. Our work can be seen in films like Steel Horizon and Night Couriers III, and TV shows like Harbor Patrol.</p>
      </div>
    </article>
  </section>

  <p class="label" style="left:926px;top:248px">FRONT/BACK</p>
  <p class="label" style="left:985px;top:708px">INSIDE</p>
</main>
</body>
</html>
```